Velvo Leaf needs a luxury packaging design

I'm starting a tea brand from the ground up. The working name as of now is Velvo Leaf. I intend for it to be a luxury loose leaf tea brand.

I want the aesthetic of it to be luxurious in nature. The color schemes that I am liking right now include black, gold, silver, rose gold and anything along that luxury feel line. One of the things I love most is UNIQUE packaging of the tea itself. I'll attach inspiration below.

I want the consumer every single time they use this product to feel like it is an experience. The person I choose will also be the person I consider for all further needs on a design basis moving forward if they would like to continue to work with me.

This is a really great opportunity to work with a luxury line that also does social good as some proceeds from each purchase will go to a mental health awareness cause.

The key is for the packaging to represent luxury, give off a unique feel that gets the consumer excited to see it and show it off to their peers on social media

Target Market(s)

The Modern Millenial, 21-40 (bullseye 28). He or she is a young professional that has a disposable income in which they do like to indulge with. They balance their demanding work schedules well and they have a work hard/play hard mindset. This professional is more likely to order their daily coffee from Brewhaven as opposed to Gus Pellery and their social media profiles are a big indicator as to their hobbies and lifestyles outside of their work environment. They enjoy shopping at stores like Ondi, Valkorn, Fenwire/FenMan and for special occasions are willing to splurge at stores like Marlow's, Maison Verdal and… They live a pretty active lifestyle and are highly influenced by social media trending products

Requirements
Must have
• Luxurious, must have exclusive look
Nice to have
• unique packaging
• viral inspired design
Should not have
• brown color, childish feel, bubble letters

```html
<!DOCTYPE html>
<html lang="en">
<head>
<meta charset="utf-8">
<title>Velvo Leaf — Tin Label Range</title>
<link rel="stylesheet" href="https://fonts.googleapis.com/css2?family=Oswald:wght@700&display=swap">
<style>
  :root {
    --backdrop: #e4e4e2;
    --tan: #c9a46d;
    --tan-stripe: #b98a55;
    --cream: #fbf7ec;
    --stripe-gold: #c3a775;
    --gold: #f3c100;
    --gold-deep: #d7a60c;
    --ochre: #d9ab2a;
    --espresso: #1b1410;
    --ink: #0b0b0b;
    --white: #ffffff;
    --label-text-tan: #b5935e;
  }
  * { margin: 0; padding: 0; box-sizing: border-box; }
  html, body {
    width: 1200px;
    height: 872px;
    overflow: hidden;
    background: var(--backdrop);
  }
  .range {
    width: 1200px;
    height: 872px;
    display: flex;
    justify-content: center;
    align-items: center;
    gap: 40px;
  }
  .label {
    position: relative;
    width: 320px;
    height: 470px;
    overflow: hidden;
  }
  .label--amber {
    background: repeating-linear-gradient(90deg,
      var(--tan) 0 5px, var(--tan-stripe) 5px 7px);
  }
  .label--noir {
    background:
      repeating-linear-gradient(0deg, rgba(0,0,0,0.22) 0 2px, transparent 2px 5px),
      linear-gradient(180deg, var(--espresso) 0%, #3a2a12 28%, var(--gold-deep) 52%, #3a2a12 76%, var(--espresso) 100%);
  }
  .label--ivory {
    background: repeating-linear-gradient(90deg,
      var(--cream) 0 9px, var(--stripe-gold) 9px 12px);
  }
  .band {
    position: absolute;
    left: -40px;
    right: -40px;
    top: 190px;
    height: 120px;
    transform: rotate(-10deg);
    display: flex;
    align-items: center;
    justify-content: center;
  }
  .label--amber .band { background: var(--ochre); }
  .label--noir .band {
    background:
      repeating-linear-gradient(0deg, rgba(0,0,0,0.08) 0 2px, transparent 2px 5px),
      linear-gradient(180deg, var(--gold-deep), var(--gold) 45%, var(--gold-deep));
  }
  .label--ivory .band { background: var(--ink); }
  .brand-name {
    font-family: "Oswald", sans-serif;
    font-weight: 700;
    font-size: 56px;
    letter-spacing: 0.5px;
    line-height: 1;
    white-space: nowrap;
  }
  .label--amber .brand-name,
  .label--ivory .brand-name { color: var(--white); }
  .label--noir .brand-name { color: var(--label-text-tan); }
</style>
</head>
<body>
  <main class="range">
    <section class="label label--amber">
      <div class="band"><span class="brand-name">Velvo Leaf</span></div>
    </section>
    <section class="label label--noir">
      <div class="band"><span class="brand-name">Velvo Leaf</span></div>
    </section>
    <section class="label label--ivory">
      <div class="band"><span class="brand-name">Velvo Leaf</span></div>
    </section>
  </main>
</body>
</html>
```